Heron Freightways LLC needs a web desigh ASAP!

We need a fully functioning web site for our trucking company!
we currently have our domain and logo.
Attached you will find our logo files and word documents with info we would like to include in our web page. (Navigation Tabs and dropdown menu)
Our domain is heronfreightways.net (from webnestly)
Our Chatterbook page is Heron Freightways LLC. You can find pictures and a little bit about our company.
our original logo is the one with bull on the left side.
Our trucking company is based in south Texas, but travel within the USA and Canada.

Target Market(s)

Logistic
Refrigerated Fleet Clients
Transportation
Trucking companies

Industry/Entity Type

Trucking Company

Coding

Coded - Design and coding required

Number of Pages Required

1 page

Font styles to use
Sans Serif

Colors
f04a51
3277b5
ffffff

Requirements
Must have
• our main email contact is Info@heronfreightways.net
• we would like see the colors of our logo. it would be nice to have a truck with our logo in the background.
• We need a web site that we can manage on our own easily.
Nice to have
• roads, highways
• get a quote module
• our inspirational web pages are:
• www.marwickhaulage.com
• www.dorvelcargo.com
• we are open to use stock photos

```html
<!DOCTYPE html>
<html lang="en">
<head>
<meta charset="utf-8">
<title>Heron Freightways LLC</title>
<link href="https://fonts.googleapis.com/css2?family=Open+Sans:ital,wght@0,400;0,600;0,700;1,400&display=swap" rel="stylesheet">
<style>
:root{
  --red:#f04a51;
  --blue:#3277b5;
  --blue-dark:#1f5e9c;
  --white:#ffffff;
  --ink:#3a3a3a;
  --muted:#6b6b6b;
  --panel:#f4f4f4;
  --footer:#2b2e33;
  --footer-text:#c9cbd0;
  --badge:#b9bcc0;
}
*{box-sizing:border-box;margin:0;padding:0}
html,body{width:960px;height:1200px;overflow:hidden}
body{font-family:"Open Sans",sans-serif;color:var(--ink);background:var(--white);position:relative}
a{color:inherit;text-decoration:none}

.site-header{height:64px;position:relative}
.brand{position:absolute;left:151px;top:16px;display:flex;align-items:center;gap:8px;font-size:22px;font-weight:700;color:var(--blue)}
.brand-dot{width:14px;height:14px;border-radius:50%;background:var(--red)}
.account{position:absolute;left:597px;top:12px;display:flex;gap:4px}
.btn{width:92px;height:22px;background:var(--red);color:var(--white);font-size:8px;font-weight:600;display:flex;align-items:center;justify-content:center;border-radius:2px}
.search{position:absolute;left:790px;top:12px}
.phone{position:absolute;left:594px;top:41px;font-size:9.5px;font-weight:600;color:var(--blue);display:flex;align-items:center;gap:5px}

.main-nav{height:36px;background:linear-gradient(#3a82c2,var(--blue-dark));position:relative}
.main-nav a{position:absolute;top:13px;color:var(--white);font-size:9.5px;font-weight:600;line-height:1}

.hero{height:240px;background:
  radial-gradient(ellipse 150px 62px at 62% 47%,rgba(226,232,240,.95) 0%,rgba(200,210,222,.75) 45%,rgba(200,210,222,0) 100%),
  radial-gradient(ellipse 60px 55px at 50% 42%,rgba(120,150,190,.8) 0%,rgba(120,150,190,0) 100%),
  radial-gradient(ellipse 240px 90px at 88% 52%,rgba(255,232,170,.95) 0%,rgba(255,214,140,0) 100%),
  linear-gradient(180deg,#f0d3a2 0%,#e3b57c 30%,#8a6a4c 52%,#b88a5e 62%,#6e5e52 78%,#4a4a4c 100%)}

.section-title{display:flex;align-items:center;font-size:19px;font-weight:600;color:var(--blue);line-height:1}
.section-title::before{content:"";width:3px;height:18px;background:var(--red);margin-right:8px}

.intro{height:247px;position:relative}
.about{position:absolute;left:151px;top:24px;width:300px}
.about .lead{margin-top:18px;font-size:11.5px;letter-spacing:.8px;line-height:18px;color:var(--muted)}
.about p{margin-top:12px;font-size:8.6px;line-height:14.3px;color:var(--muted)}
.partners{position:absolute;left:481px;top:24px;width:330px}
.partner-grid{margin-top:24px;display:grid;grid-template-columns:repeat(3,1fr);row-gap:20px;column-gap:14px}
.partner-grid span{height:28px;display:flex;align-items:center;justify-content:center}
.partner-grid i{display:block;width:80px;height:22px;border-radius:3px;background:var(--badge)}

.services{height:413px;background:var(--panel);position:relative}
.services .section-title{position:absolute;left:405px;top:28px}
.cards{position:absolute;left:151px;top:68px;display:flex;gap:9px}
.card{width:214px;height:300px;background:var(--white);border:1px solid #e3e3e3;position:relative}
.card-photo{height:129px}
.photo-1{background:linear-gradient(160deg,#2d5ea8,#8fa4bf 60%,#5a6470)}
.photo-2{background:linear-gradient(160deg,#c9d3dc,#e9ecef 50%,#9aa3ab)}
.photo-3{background:linear-gradient(160deg,#9bb0c6,#e1b27d 55%,#6a5d54)}
.card h3{margin:16px 0 0 7px;font-size:11.5px;font-weight:400;color:#2a2a2a;position:relative}
.card h3::before{content:"";position:absolute;left:0;top:-7px;width:19px;height:2px;background:var(--red)}
.card p{margin:7px 8px 0 7px;font-size:9px;line-height:14.4px;color:var(--muted)}
.read-more{position:absolute;right:10px;bottom:4px;font-size:9px;color:var(--red)}

.site-footer{height:200px;background:var(--footer);position:relative;color:var(--footer-text)}
.col{position:absolute;top:30px}
.col h4{font-size:10.5px;font-weight:600;color:#e4e6ea;margin-bottom:10px;line-height:14px}
.col li{list-style:none;font-size:7.6px;font-weight:600;line-height:12px;margin-bottom:9.5px}
.newsletter{left:151px;width:180px}
.newsletter p{font-size:9.3px;line-height:14.5px}
.subscribe{margin-top:14px;display:flex;height:26px}
.subscribe span{width:137px;background:#454a52;font-size:8.6px;font-style:italic;display:flex;align-items:center;padding-left:10px}
.subscribe b{width:35px;background:var(--blue);display:flex;align-items:center;justify-content:center}
.links{left:357px}
.news{left:493px}
.contact{left:652px}
.contact li{font-size:7.8px;margin-bottom:8.5px}
.contact li.strong{font-size:9.3px;color:var(--white)}
.contact li.social{margin-bottom:0}
.social{display:flex;align-items:center;gap:6px;font-size:8px;font-weight:600}
.social i{width:17px;height:17px;background:var(--blue);display:block}
.legal{position:absolute;left:151px;right:150px;top:179px;border-top:1px solid #454a52;padding-top:7px;font-size:6.5px;font-weight:600;color:#7b7f86}
</style>
</head>
<body>
<header class="site-header">
  <a class="brand" href="#"><span class="brand-dot"></span>Heron Freightways</a>
  <div class="account"><a class="btn" href="#">LOGIN</a><a class="btn" href="#">SIGN UP</a></div>
  <svg class="search" width="20" height="20" viewBox="0 0 20 20" aria-label="Search"><circle cx="8" cy="8" r="6" fill="none" stroke="#3277b5" stroke-width="2"/><line x1="12.5" y1="12.5" x2="18" y2="18" stroke="#3277b5" stroke-width="2.2"/></svg>
  <div class="phone">
    <svg width="11" height="11" viewBox="0 0 24 24"><path fill="#3277b5" d="M6.6 10.8a15 15 0 0 0 6.6 6.6l2.2-2.2c.3-.3.7-.4 1-.2 1.1.4 2.3.6 3.6.6.6 0 1 .4 1 1V20c0 .6-.4 1-1 1A17 17 0 0 1 3 4c0-.6.4-1 1-1h3.5c.6 0 1 .4 1 1 0 1.3.2 2.5.6 3.6.1.3 0 .7-.2 1z"/></svg>
    1 - 877- 555- 0148 OR (956) 555-0172
  </div>
</header>

<nav class="main-nav">
  <a href="#" style="left:151px">HOME</a>
  <a href="#" style="left:217px">ABOUT US</a>
  <a href="#" style="left:301px">SOLUTIONS</a>
  <a href="#" style="left:392px">EXPERTISE</a>
  <a href="#" style="left:477px">INVESTORS</a>
  <a href="#" style="left:565px">CAREERS</a>
  <a href="#" style="left:643px">CONTACT</a>
</nav>

<div class="hero" role="img" aria-label="White branded semi truck with a silver-blue cab driving along a rural highway at sunset, golden hills behind"></div>

<section class="intro">
  <div class="about">
    <h2 class="section-title">ABOUT US</h2>
    <p class="lead">We carry and deliver almost any type of temperature sensitive products anywhere in the United States.</p>
    <p>Heron Freightways LLC currently has the very latest in transport refrigeration technology. Our brand new trucks and professional looking equipment set the standard with outstanding efficiency and reliability paired with superior temperature control.</p>
    <p>We offer quality and reliability. We've got you and your business covered day and night, from origin to destination.</p>
  </div>
  <div class="partners">
    <h2 class="section-title">OUR PARTNERS</h2>
    <div class="partner-grid">
      <span><i></i></span><span><i></i></span><span><i></i></span>
      <span><i></i></span><span><i></i></span><span><i></i></span>
    </div>
  </div>
</section>

<section class="services">
  <h2 class="section-title">OUR SERVICES</h2>
  <div class="cards">
    <article class="card">
      <div class="card-photo photo-1" role="img" aria-label="Blue box truck on a motorway"></div>
      <h3>SUPPLY CHAIN MANANGEMENT</h3>
      <p>Single-origin coffee small batch PBR&amp;B pork belly +1. VHS mlkshk hashtag +1. Humble-brag pitchfork hella small batch godard, bushwick blog irony put a bird on it keffiyeh migas church-key PBR&amp;B. ut a bird on it gastropub 3 wolf moon blog, meditation try-hard yr occupy fanny pack waistcoat health goth fashion axe.</p>
      <a class="read-more" href="#">READ MORE</a>
    </article>
    <article class="card">
      <div class="card-photo photo-2" role="img" aria-label="Truck driver with a clipboard standing beside a white rig"></div>
      <h3>REFRIDGERATION SPECIALISTS</h3>
      <p>Single-origin coffee small batch PBR&amp;B pork belly +1. VHS mlkshk hashtag +1. Humble-brag pitchfork hella small batch godard, bushwick blog irony put a bird on it keffiyeh migas church-key PBR&amp;B. ut a bird on it gastropub 3 wolf moon blog, meditation try-hard yr occupy fanny pack waistcoat health goth fashion axe.</p>
      <a class="read-more" href="#">READ MORE</a>
    </article>
    <article class="card">
      <div class="card-photo photo-3" role="img" aria-label="Red semi truck on an open highway at dusk"></div>
      <h3>ACROSS USA &amp; CANANDA</h3>
      <p>Single-origin coffee small batch PBR&amp;B pork belly +1. VHS mlkshk hashtag +1. Humble-brag pitchfork hella small batch godard, bushwick blog irony put a bird on it keffiyeh migas church-key PBR&amp;B. ut a bird on it gastropub 3 wolf moon blog, meditation try-hard yr occupy fanny pack waistcoat health goth fashion axe.</p>
      <a class="read-more" href="#">READ MORE</a>
    </article>
  </div>
</section>

<footer class="site-footer">
  <div class="col newsletter">
    <h4>NEWSLETTER SUBSCRIBE</h4>
    <p>Subscribe to our newsletter and we will inform you about projects and developements.</p>
    <div class="subscribe"><span>Your Email ....</span><b><svg width="12" height="9" viewBox="0 0 12 9"><rect x=".5" y=".5" width="11" height="8" fill="none" stroke="#fff"/><path d="M.5.5 6 5l5.5-4.5" fill="none" stroke="#fff"/></svg></b></div>
  </div>
  <div class="col links">
    <h4>QUICK LINKS</h4>
    <ul><li>&gt; ABOUT US</li><li>&gt; COMPANY HISTORY</li><li>&gt;COMPANY EVENTS</li><li>&gt; DISTRIBUTIONS</li><li>&gt; HOW WE WORK</li></ul>
  </div>
  <div class="col news">
    <h4>INDUSTRY NEWS</h4>
    <ul><li>&gt; TRANSPORTATION</li><li>&gt; REFRIDGERATION STANDARDS</li><li>&gt; RAIL FREIGHT</li><li>&gt; AIR FREIGHT</li><li>&gt; LARGE PROJECTS</li></ul>
  </div>
  <div class="col contact">
    <h4>CONTACT US</h4>
    <ul>
      <li>4120 N. MESA BLVD. ALAMO, TX 78516</li>
      <li class="strong">TOLL FREE: 1-877-555-0148</li>
      <li class="strong">LOCAL NUMBER: (956) 555-0172</li>
      <li>DISPATCH@HERONFREIGHTWAYS.NET</li>
      <li>INFO@HERONFREIGHTWAYS.NET</li>
      <li class="social"><i></i>Chatterbook</li>
    </ul>
  </div>
  <div class="legal">HERON FREIGHTWAYS 2016, ALL RIGHTS RESERVED</div>
</footer>
</body>
</html>
```